A start up special flyer design!

Hi All - Have updated the attachment content - This is the info required for the designs.
I need a catchy flyer to send out to a few areas to advertise the start of my plumbing business!
The flyer will contain an offer for customers, which will need to have some key details on it. See attached. Feel free to fit these criteria into the flyer given your knowledge on design and messaging principles. Key thing to get across to customers is the discount and special offer, and that it is a start up offer.
I have a logo that needs to be on the flyer as well - let me know what format you require and I will send through to you.
The color scheme needs to be blue / grey / black / white.
Let me know if you have any questions.
I

```html
<!DOCTYPE html>
<html lang="en">
<head>
<meta charset="utf-8">
<title>Marlow Pipe Plumbing – Start-up Offer Flyer</title>
<link href="https://fonts.googleapis.com/css2?family=Oswald:wght@400;500&family=Source+Sans+3:wght@400&display=swap" rel="stylesheet">
<style>
  :root{
    --navy:#163f73;
    --navy-deep:#0f3260;
    --blue:#1f65ad;
    --cyan:#2fa9e0;
    --sky:#7fcdee;
    --paper:#f3f3f3;
    --white:#ffffff;
    --grey:#5a5f66;
    --dash:#9aa0a6;
  }
  *{margin:0;padding:0;box-sizing:border-box}
  html,body{width:1200px;height:893px;overflow:hidden;background:var(--paper)}
  .flyer{position:relative;width:1200px;height:893px;overflow:hidden;background:var(--paper);font-family:'Oswald',sans-serif}
  .artwork{position:absolute;inset:0}
  .brand{position:absolute;left:60px;top:112px;width:360px;display:flex;align-items:center;gap:14px}
  .brand-dot{width:34px;height:34px;border-radius:50%;background:var(--blue);flex:none}
  .brand-name{font-family:'Oswald',sans-serif;font-weight:500;font-size:34px;line-height:1.05;color:var(--blue);letter-spacing:1px;text-transform:uppercase}
  .tagline{position:absolute;left:570px;top:38px;height:58px;display:flex;align-items:center;color:var(--white);font-weight:500;font-size:34px;letter-spacing:3.5px;text-transform:uppercase;white-space:nowrap}
  .services{position:absolute;left:60px;top:300px;color:var(--navy);font-weight:500;font-size:37px;line-height:49px;text-transform:uppercase;letter-spacing:-.3px;white-space:nowrap}
  .contacts{position:absolute;left:42px;top:560px;list-style:none}
  .contacts li{display:flex;align-items:center;gap:18px;height:52px;color:var(--white);font-weight:500;font-size:30px;white-space:nowrap}
  .contacts svg{width:34px;height:34px;flex:none}
  .offers{position:absolute;left:12px;top:744px;display:flex;gap:14px}
  .offer{height:142px;border:1.5px dashed var(--dash);background:var(--white);display:flex;flex-direction:column;justify-content:center;align-items:center;text-align:center;color:var(--navy);overflow:hidden}
  .offer-1{width:383px}
  .offer-2{width:382px}
  .offer-3{width:384px}
  .offer-title{font-weight:500;font-size:30px;line-height:36px;letter-spacing:-.5px;white-space:nowrap}
  .offer-discount{display:flex;align-items:baseline;gap:12px;font-weight:500;white-space:nowrap}
  .offer-discount .big{font-size:56px;line-height:62px;letter-spacing:-2px}
  .offer-discount .small{font-size:26px;letter-spacing:-.5px}
  .offer-terms{margin-top:10px;font-family:'Source Sans 3',sans-serif;font-size:14px;color:var(--grey);white-space:nowrap}
</style>
</head>
<body>
<main class="flyer">
  <svg class="artwork" width="1200" height="893" viewBox="0 0 1200 893">
    <defs>
      <linearGradient id="bannerFill" x1="0" x2="1">
        <stop offset="0" stop-color="#123a6b"/>
        <stop offset="1" stop-color="#2a73b8"/>
      </linearGradient>
      <linearGradient id="waveNavy" x1="0" x2="1">
        <stop offset="0" stop-color="#123c6e"/>
        <stop offset="1" stop-color="#1d5d9c"/>
      </linearGradient>
      <linearGradient id="waveSky" x1="0" x2="1">
        <stop offset="0" stop-color="#4fb6e4"/>
        <stop offset="1" stop-color="#8fd3ef"/>
      </linearGradient>
      <radialGradient id="photoMain" cx=".55" cy=".45" r=".6">
        <stop offset="0" stop-color="#e9eef2"/>
        <stop offset=".55" stop-color="#7fa4cf"/>
        <stop offset="1" stop-color="#2f5f99"/>
      </radialGradient>
      <radialGradient id="photoDrain" cx=".5" cy=".5" r=".6">
        <stop offset="0" stop-color="#d7eefa"/>
        <stop offset="1" stop-color="#3d86c4"/>
      </radialGradient>
      <radialGradient id="photoPipes" cx=".5" cy=".5" r=".6">
        <stop offset="0" stop-color="#cfd6de"/>
        <stop offset="1" stop-color="#55708f"/>
      </radialGradient>
    </defs>

    <circle cx="190" cy="-120" r="412" fill="none" stroke="#8fd3ef" stroke-width="6"/>
    <circle cx="190" cy="-120" r="402" fill="var(--white)" stroke="var(--cyan)" stroke-width="12"/>

    <polygon points="540,35 1200,35 1200,98 516,98" fill="url(#bannerFill)"/>

    <path d="M0,476 C150,452 300,478 460,548 C590,606 700,672 860,700 L1200,690 L1200,740 L0,740 Z" fill="url(#waveNavy)"/>
    <path d="M430,572 C560,560 660,600 770,660 C850,702 950,706 1200,650 L1200,704 C1000,720 880,728 780,708 C640,680 540,620 430,572 Z" fill="url(#waveSky)"/>

    <circle cx="962" cy="405" r="262" fill="#cfe9f6"/>
    <circle cx="962" cy="405" r="252" fill="url(#photoMain)" stroke="var(--sky)" stroke-width="6" role="img" aria-label="Photo of a plumber in a blue cap tightening a sink drain pipe with a red wrench"/>

    <circle cx="753" cy="579" r="88" fill="url(#photoDrain)" stroke="#bfe6f7" stroke-width="6" role="img" aria-label="Close-up photo of water swirling into a drain"/>

    <circle cx="978" cy="656" r="94" fill="url(#photoPipes)" stroke="var(--cyan)" stroke-width="6" role="img" aria-label="Photo of gloved hands fitting a pipe valve"/>

    <rect x="0" y="740" width="1200" height="153" fill="var(--white)"/>
  </svg>

  <div class="brand">
    <span class="brand-dot"></span>
    <span class="brand-name">Marlow Pipe<br>Plumbing</span>
  </div>

  <div class="tagline">Quality work at a decent price</div>

  <h1 class="services">All plumbing, draining, and<br>gasfitting works<br>local plumber</h1>

  <ul class="contacts">
    <li>
      <svg viewBox="0 0 34 34"><circle cx="17" cy="17" r="16" fill="#fff"/><path d="M11 9c1.3-.8 2.4-.5 3 .8l1.2 2.6c.4 1 .1 1.8-.7 2.4l-1 .7c.9 2 2.4 3.6 4.4 4.6l.8-1c.6-.8 1.5-1 2.4-.6l2.6 1.2c1.2.6 1.5 1.8.7 3-1.3 1.8-3.2 2.5-5.3 1.7-4.6-1.7-8-5.2-9.6-9.8-.7-2 .1-3.9 1.5-5.6z" fill="var(--navy)"/></svg>
      <span>0400 218 764</span>
    </li>
    <li>
      <svg viewBox="0 0 34 34"><circle cx="17" cy="17" r="16" fill="#fff"/><rect x="8.5" y="11" width="17" height="12" rx="1.5" fill="none" stroke="var(--navy)" stroke-width="2"/><path d="M9 12l8 6.5 8-6.5" fill="none" stroke="var(--navy)" stroke-width="2"/></svg>
      <span>hello@marlowpipeplumbing.com</span>
    </li>
    <li>
      <svg viewBox="0 0 34 34"><circle cx="17" cy="17" r="16" fill="#fff"/><g fill="none" stroke="var(--navy)" stroke-width="1.8"><circle cx="17" cy="17" r="10"/><ellipse cx="17" cy="17" rx="4.5" ry="10"/><path d="M7 17h20M9 12h16M9 22h16"/></g></svg>
      <span>www.marlowpipeplumbing.com</span>
    </li>
  </ul>

  <section class="offers">
    <article class="offer offer-1">
      <div class="offer-discount"><span class="big">15% OFF</span><span class="small">your overall bill</span></div>
      <p class="offer-terms">Offer valid between 15 August 2016 to 15 October 2016.</p>
    </article>
    <article class="offer offer-2">
      <p class="offer-title">No GST payable, saving you<br>additional 10% on your bill</p>
      <p class="offer-terms">Offer valid until 30 September 2016.</p>
    </article>
    <article class="offer offer-3">
      <p class="offer-title">Plus, a free hot water health<br>check and replacement quote</p>
      <p class="offer-terms">Quote valid for 12 months from the quote date.</p>
    </article>
  </section>
</main>
</body>
</html>
```